Quellmark Exteriors Needs a New Website!

We are an exteriors company specializing in vinyl siding, Morten Calloway siding, aluminum soffit/fascia, trough. We do new construction work as well as renovations. We also build detached garages.
You can view our current website at www.quellmarkbuilders.ca
I want to completely overhaul the website.
Our services are different now as we no longer do new home construction as well as we do not do the snow clearing.
I want to focus on 2 things in particular on the website:

1/ Exterior renovations

2/ Detached Garage construction.

I have included our logo in the attached files to use as well.

Some features we would like:

1/ Be able to easily attach a video from Youtube/Vimeo to highlight a product or service
2/ Quick chat or contact button that we can talk to a potential client quickly
3/ Meet the Team page that is interesting and fresh
4/ Place for us to put in helpful exterior tips/suggestions for homeowners.

Content is not important, but looking for the best design that will attract people once they click on our page and want to renovate with us.

Target Market(s)

People looking for renovations on their home, people looking to build a detached garage.

Industry/Entity Type

Residential Construction

Coding

Coded - Design and coding required

Number of Pages Required

5+ page

Font styles to use
Sans Serif

Requirements
Must have
• Fresh and exciting home page.

Simple design. Don't want it over complicated or too much information to confuse the potential client.

Easy way to contact us.

Meet the team page that instills confidence
Nice to have
• Colour of website to go off our logo. Doesn't need to be an exact match, but something that goes well with our blue and grey.

```html
<!DOCTYPE html>
<html lang="en">
<head>
<meta charset="utf-8">
<title>Quellmark Exteriors</title>
<link rel="stylesheet" href="https://fonts.googleapis.com/css2?family=Open+Sans:wght@400;600;700;800&display=swap">
<style>
:root{
  --blue:#1f74c9;
  --blue-dark:#155a9e;
  --grey-dark:#3b3b3d;
  --grey-nav:#4a4a4c;
  --grey-footer:#2d2d2f;
  --grey-text:#666;
  --light:#f5f5f5;
  --white:#fff;
  --gold:#f3b51b;
}
*{box-sizing:border-box;margin:0;padding:0}
html,body{width:1200px;height:4496px;overflow:hidden}
body{font-family:"Open Sans",Arial,sans-serif;color:#333;background:var(--white);position:relative}
.section{position:absolute;left:0;width:1200px}
.btn{display:inline-block;background:var(--blue);color:var(--white);font-size:14px;font-weight:600;padding:11px 24px;border-radius:4px}
.section-title{text-align:center;font-size:30px;font-weight:700;color:#333;letter-spacing:.5px}
.section-title::after{content:"";display:block;width:60px;height:3px;background:var(--blue);margin:14px auto 0}

/* header */
.topbar{top:0;height:68px;background:var(--white)}
.call{position:absolute;left:110px;top:18px;display:flex;gap:10px;align-items:center;font-size:13px}
.call b{color:var(--blue);display:block;font-size:12px}
.brand{position:absolute;left:50%;top:16px;transform:translateX(-50%);display:flex;align-items:center;gap:10px}
.brand-dot{width:30px;height:30px;border-radius:50%;background:var(--blue)}
.brand-name{font-size:24px;font-weight:800;color:var(--grey-dark);letter-spacing:.5px}
.topbar .btn{position:absolute;right:110px;top:14px;border-radius:20px;font-size:13px;padding:10px 20px}
.nav{top:68px;height:52px;background:var(--grey-nav)}
.nav ul{list-style:none;display:flex;justify-content:center;height:52px}
.nav li{color:var(--white);font-size:14px;padding:0 30px;line-height:52px}
.nav li.active{background:#6a6a6c}

/* hero */
.hero{top:120px;height:640px;background:linear-gradient(180deg,#7fb6e6 0%,#cfe3f3 45%,#8d9a85 75%,#5f6b58 100%)}
.hero-circle{position:absolute;left:80px;top:80px;width:370px;height:370px;border-radius:50%;background:rgba(31,116,201,.78);color:var(--white);text-align:center;padding-top:100px}
.hero-circle small{font-size:19px;font-weight:600;letter-spacing:1px}
.hero-circle h1{font-size:31px;font-weight:800;line-height:1.1;margin:4px 0 10px}
.hero-circle p{font-size:12px;width:260px;margin:0 auto 18px;opacity:.9}
.hero-circle .btn{background:var(--blue-dark);font-size:12px;padding:9px 18px}

/* about */
.about{top:760px;height:440px;display:flex}
.about-text{width:600px;background:var(--grey-dark);color:var(--white);padding:70px 60px 0 110px}
.about-text h2{font-size:26px;font-weight:700;margin-bottom:6px}
.about-text h2::after{content:"";display:block;width:50px;height:3px;background:var(--blue);margin-top:10px}
.about-text p{font-size:13px;line-height:1.6;margin-top:18px;color:#ddd}
.about-text .btn{margin-top:26px;font-size:12px;padding:9px 20px}
.about-photo{width:600px;background:linear-gradient(160deg,#b7cee6 0%,#8d98a3 45%,#6c7d58 100%)}

/* services */
.services{top:1200px;height:1020px;background:var(--white);overflow:hidden}
.services .section-title{margin-top:70px}
.faint-ring{position:absolute;left:380px;top:240px;width:440px;height:440px;border-radius:50%;border:36px solid #f2f2f2}
.service-grid{position:relative;display:grid;grid-template-columns:repeat(3,280px);column-gap:90px;row-gap:60px;justify-content:center;margin-top:70px}
.service{text-align:center}
.service .ico{width:100px;height:100px;border-radius:50%;border:2px solid #bbb;margin:0 auto 14px;display:flex;align-items:center;justify-content:center;background:var(--white)}
.service h3{font-size:13px;font-weight:700;color:#333;letter-spacing:.5px}
.service p{font-size:12px;color:var(--grey-text);line-height:1.55;margin-top:10px}
.services .center{position:relative;text-align:center;margin-top:60px}

/* projects */
.projects{top:2220px;height:940px;background:var(--light)}
.projects .section-title{margin-top:90px}
.project-grid{position:absolute;left:0;top:200px;width:1200px;display:grid;grid-template-columns:repeat(4,1fr);grid-template-rows:300px 290px;gap:10px}
.project-grid div{border-radius:0}
.p1{background:linear-gradient(180deg,#6fa6d8,#c7b08a)}
.p2{background:linear-gradient(180deg,#c7d9ea,#e9eef2)}
.p3{background:linear-gradient(180deg,#4f8fd0,#aab3bb)}
.p4{background:linear-gradient(180deg,#8ab4dc,#d9d1c8)}
.p5{background:linear-gradient(180deg,#dfe6ea,#c9b08c)}
.p6{background:linear-gradient(180deg,#a9c4dd,#7f8c97)}
.p7{grid-column:span 2;background:linear-gradient(180deg,#5d97d4,#b7bfc6 60%,#6c7a5c)}
.projects .center{position:absolute;left:0;width:100%;text-align:center;top:820px}

/* why */
.why{top:3160px;height:620px;background:linear-gradient(180deg,#3c4350,#2e333b);color:var(--white)}
.why .section-title{color:var(--white);margin-top:70px}
.why-grid{display:grid;grid-template-columns:repeat(3,300px);column-gap:50px;row-gap:70px;justify-content:center;margin-top:70px}
.why-item{display:flex;gap:16px}
.why-item .ico{flex:0 0 80px;height:80px;border-radius:50%;border:2px solid var(--white);display:flex;align-items:center;justify-content:center}
.why-item h3{font-size:13px;font-weight:700;color:#7ab8f0;letter-spacing:.3px}
.why-item p{font-size:11.5px;line-height:1.55;color:#ddd;margin-top:6px}

/* testimonials */
.clients{top:3780px;height:340px;background:var(--white);text-align:center}
.clients .section-title{margin-top:55px}
.quote{width:820px;margin:40px auto 0;font-size:13px;line-height:1.6;color:var(--grey-text);position:relative}
.quote::before{content:"\201C";position:absolute;left:-30px;top:-14px;font-size:46px;color:#999}
.clients h4{color:var(--blue);font-size:17px;font-weight:700;margin-top:16px}
.stars{color:var(--gold);font-size:16px;letter-spacing:2px}
.dots{margin-top:14px;display:flex;justify-content:center;gap:8px}
.dots span{width:7px;height:7px;border-radius:50%;background:#bbb}
.dots span:first-child{background:var(--grey-dark)}

/* footer */
.footer{top:4120px;height:340px;background:var(--grey-footer);color:#ccc}
.f-brand{position:absolute;left:110px;top:50px;width:250px}
.f-brand .brand-name{color:var(--white);font-size:22px}
.f-brand p{font-size:12px;line-height:1.6;margin-top:18px}
.f-brand .more{color:var(--blue);font-size:12px;margin-top:10px;display:block}
.f-col{position:absolute;top:50px}
.f-col h5{color:var(--white);font-size:13px;font-weight:700;margin-bottom:16px}
.f-col li{list-style:none;font-size:12px;line-height:1.8}
.f-links{left:430px}
.f-info{left:585px}
.f-info li{display:flex;gap:8px;align-items:center}
.social{display:flex;gap:6px;margin-top:10px}
.social span{width:18px;height:18px;border-radius:50%;background:#c0392b}
.contact-form{position:absolute;left:800px;top:4012px;width:265px;height:440px;background:var(--blue);padding:0 22px;box-shadow:0 0 0 3px var(--blue-dark)}
.contact-form h5{color:var(--white);text-align:center;font-size:15px;font-weight:700;padding:12px 0 20px;border-bottom:1px solid rgba(255,255,255,.3);margin:0 -22px 16px}
.field{background:var(--white);height:32px;margin-bottom:12px;font-size:11px;color:#999;padding:8px 10px}
.field.msg{height:110px}
.contact-form .submit{display:block;margin:16px auto 0;width:120px;text-align:center;background:var(--blue-dark);color:var(--white);font-size:12px;padding:9px 0;border-radius:3px}
.copyright{top:4460px;height:36px;background:var(--blue);color:var(--white);font-size:11px;line-height:36px;padding-left:110px}
</style>
</head>
<body>

<header class="section topbar">
  <div class="call">
    <svg width="26" height="26" viewBox="0 0 24 24" fill="none" stroke="#1f74c9" stroke-width="2"><path d="M5 3h4l2 5-3 2a11 11 0 0 0 6 6l2-3 5 2v4a2 2 0 0 1-2 2A17 17 0 0 1 3 5a2 2 0 0 1 2-2z"/></svg>
    <div><b>Call us Now</b>780-555-0142</div>
  </div>
  <div class="brand"><span class="brand-dot"></span><span class="brand-name">QUELLMARK EXTERIORS</span></div>
  <span class="btn">Request a Quote</span>
</header>

<nav class="section nav">
  <ul><li class="active">Home</li><li>About us</li><li>Services</li><li>Projects</li><li>Contact us</li>
  <li><svg width="14" height="14" viewBox="0 0 24 24" fill="none" stroke="#fff" stroke-width="3"><circle cx="10" cy="10" r="7"/><path d="M15 15l6 6"/></svg></li></ul>
</nav>

<section class="section hero" role="img" aria-label="Photo of a renovated two-storey house with stone and siding exterior under blue sky">
  <div class="hero-circle">
    <small>EXPERIENCE THE</small>
    <h1>QUELLMARK<br>DIFFERENCE</h1>
    <p>Simple, lasting exterior renovations and detached garages built right.</p>
    <span class="btn">Request a Quote</span>
  </div>
</section>

<section class="section about">
  <div class="about-text">
    <h2>ABOUT US</h2>
    <p>Lorem Ipsum is simply dummy text of the printing and typesetting industry. Lorem Ipsum has been the industry's standard dummy text ever since the 1500s, when an unknown printer took a galley of type and scrambled it to make a type specimen book.</p>
    <p>It has survived not only five centuries, but also the leap into electronic typesetting, remaining essentially unchanged.</p>
    <span class="btn">Read More</span>
  </div>
  <div class="about-photo" role="img" aria-label="Photo of a house under renovation with scaffolding and a lift"></div>
</section>

<section class="section services">
  <h2 class="section-title">OUR SERVICES</h2>
  <div class="faint-ring"></div>
  <div class="service-grid">
    <div class="service"><div class="ico"><svg width="48" height="40" viewBox="0 0 48 40" fill="none" stroke="#1f74c9" stroke-width="2"><path d="M4 20L24 4l20 16M10 16v20h28V16"/><path d="M20 36V26h8v10"/></svg></div>
      <h3>ROOFING</h3><p>Regular maintenance and repairs can extend the life of a roof. However, at some point, re-roofing your home is the preferred option. Re-roofing replaces your current roof with a completely new one.</p></div>
    <div class="service"><div class="ico"><svg width="46" height="40" viewBox="0 0 46 40" fill="none" stroke="#1f74c9" stroke-width="2"><path d="M4 8h38M4 16h38M4 24h38M4 32h38"/></svg></div>
      <h3>SIDING</h3><p>Siding, also known as wall cladding, is an exterior material which is applied to the walls of a building to protect the property from the damaging effects of weather and to provide insulation.</p></div>
    <div class="service"><div class="ico"><svg width="46" height="40" viewBox="0 0 46 40" fill="none" stroke="#1f74c9" stroke-width="2"><path d="M4 30L38 8l4 6L8 36z"/><path d="M12 26l4 5M20 21l4 5M28 16l4 5"/></svg></div>
      <h3>SOFFIT &amp; FASCIA</h3><p>Soffit is most commonly known to bridge the gap between your siding and roofline, but it can also be used under porches, arches, columns, and more on exterior flight of stairs.</p></div>
    <div class="service"><div class="ico"><svg width="46" height="40" viewBox="0 0 46 40" fill="none" stroke="#1f74c9" stroke-width="2"><path d="M4 8h38l-4 10H8z"/><path d="M30 18v18M30 36h8"/></svg></div>
      <h3>GUTTERS</h3><p>We have installed a number of robust gutter systems and gutter toppers to keep homes across the region dry through every season.</p></div>
    <div class="service"><div class="ico"><svg width="46" height="40" viewBox="0 0 46 40" fill="none" stroke="#1f74c9" stroke-width="2"><path d="M10 34L30 6l8 6L18 36z"/><path d="M10 34l-2 4 6-2"/></svg></div>
      <h3>TRIMS</h3><p>Trim and molding distinguish a single detached family home, townhouse, or condo complex from the rest.</p></div>
    <div class="service"><div class="ico"><svg width="46" height="40" viewBox="0 0 46 40" fill="none" stroke="#1f74c9" stroke-width="2"><path d="M8 36V12l14-8v32M22 14h16v22"/><path d="M12 18h6M12 24h6M12 30h6M26 20h8M26 26h8"/></svg></div>
      <h3>EXTERIOR INSULATION</h3><p>The amount of energy your household consumes is directly related to the ability of heat to get in and out of your home.</p></div>
  </div>
  <div class="center"><span class="btn">View All Services</span></div>
</section>

<section class="section projects">
  <h2 class="section-title">RECENTLY PROJECTS</h2>
  <div class="project-grid">
    <div class="p1" role="img" aria-label="Photo of a house with a new wooden deck"></div>
    <div class="p2" role="img" aria-label="Photo of a house exterior in winter"></div>
    <div class="p3" role="img" aria-label="Photo of a modern home with new siding"></div>
    <div class="p4" role="img" aria-label="Photo of a house under exterior renovation with scaffolding"></div>
    <div class="p5" role="img" aria-label="Photo of a new house frame under construction"></div>
    <div class="p6" role="img" aria-label="Photo of a two-storey home with grey siding"></div>
    <div class="p7" role="img" aria-label="Photo of a large finished home with attached garage"></div>
  </div>
  <div class="center"><span class="btn">View All Projects</span></div>
</section>

<section class="section why" role="img" aria-label="Darkened photo of a residential street as background">
  <h2 class="section-title">WHY CHOOSE US?</h2>
  <div class="why-grid">
    <div class="why-item"><div class="ico"><svg width="36" height="36" viewBox="0 0 24 24" fill="none" stroke="#fff" stroke-width="1.6"><circle cx="12" cy="9" r="6"/><path d="M8 14l-2 8 6-3 6 3-2-8"/></svg></div>
      <div><h3>CERTIFIED EXPERIENCE</h3><p>Having professionals do the job gives you the confidence that the job will be done right, on budget, and on time.</p></div></div>
    <div class="why-item"><div class="ico"><svg width="36" height="36" viewBox="0 0 24 24" fill="none" stroke="#fff" stroke-width="1.6"><path d="M3 5h13v9H8l-4 3v-3H3z"/><path d="M18 9h3v9h-1v3l-4-3h-5"/></svg></div>
      <div><h3>SUPERIOR COMMUNICATION</h3><p>Taking the time to explain the construction process and promptly answering the phone or email is what sets us apart from others.</p></div></div>
    <div class="why-item"><div class="ico"><svg width="36" height="36" viewBox="0 0 24 24" fill="none" stroke="#fff" stroke-width="1.6"><path d="M3 12l9-9h8v8l-9 9z"/><circle cx="16" cy="8" r="1.5"/></svg></div>
      <div><h3>COMPETITIVE PRICING</h3><p>Although we offer the best in services, we won't leave your budget in the red. We also take a solid value in our renovation decisions.</p></div></div>
    <div class="why-item"><div class="ico"><svg width="36" height="36" viewBox="0 0 24 24" fill="none" stroke="#fff" stroke-width="1.6"><circle cx="12" cy="12" r="9"/><path d="M8 14s1.5 2 4 2 4-2 4-2M9 9h.01M15 9h.01"/></svg></div>
      <div><h3>GUARANTEED SATISFACTION</h3><p>We won't leave unless you are happy with a robust finish. Whether materials or services, we ensure you are satisfied with every step.</p></div></div>
    <div class="why-item"><div class="ico"><svg width="36" height="36" viewBox="0 0 24 24" fill="none" stroke="#fff" stroke-width="1.6"><path d="M12 3l8 3v6c0 5-4 8-8 9-4-1-8-4-8-9V6z"/><path d="M8 12l3 3 5-5"/></svg></div>
      <div><h3>SAFETY CONSCIENCE</h3><p>Full certification, safety insurance and proper coverage on all workers gives you peace of mind that the job will be done safely.</p></div></div>
    <div class="why-item"><div class="ico"><svg width="36" height="36" viewBox="0 0 24 24" fill="none" stroke="#fff" stroke-width="1.6"><path d="M12 3l2.6 5.5 6 .8-4.4 4.2 1.1 6L12 16.6 6.7 19.5l1.1-6L3.4 9.3l6-.8z"/></svg></div>
      <div><h3>UNRIVALLED QUALITY</h3><p>Our general goal is our committed pursuit of a "top of the line" job each and every time.</p></div></div>
  </div>
</section>

<section class="section clients">
  <h2 class="section-title">OUR CLIENTS SAY`S</h2>
  <p class="quote">Lorem Ipsum is simply dummy text of the printing and typesetting industry. Lorem Ipsum has been the industry's standard dummy text ever since the 1500s, when an unknown printer took a galley of type and scrambled it to make a type specimen book. It has survived not only five centuries, but also the leap into electronic typesetting, remaining essentially unchanged.</p>
  <h4>DARREN WHITFIELD</h4>
  <div class="stars">★★★★★</div>
  <div class="dots"><span></span><span></span><span></span></div>
</section>

<footer class="section footer">
  <div class="f-brand">
    <span class="brand-name">QUELLMARK EXTERIORS</span>
    <p>Lorem Ipsum is simply dummy text of the printing and typesetting industry. Lorem Ipsum has been the industry's standard dummy text ever since the 1500s.</p>
    <span class="more">Read More</span>
  </div>
  <div class="f-col f-links"><h5>QUICK LINKS</h5><ul><li>Home</li><li>About us</li><li>Services</li><li>Projects</li><li>Contact us</li></ul></div>
  <div class="f-col f-info"><h5>CONTACT INFO</h5><ul>
    <li><svg width="11" height="11" viewBox="0 0 24 24" fill="#ccc"><path d="M5 3h4l2 5-3 2a11 11 0 0 0 6 6l2-3 5 2v4a2 2 0 0 1-2 2A17 17 0 0 1 3 5a2 2 0 0 1 2-2z"/></svg>780-555-0142</li>
    <li><svg width="11" height="11" viewBox="0 0 24 24" fill="none" stroke="#ccc" stroke-width="2"><rect x="3" y="5" width="18" height="14"/><path d="M3 6l9 7 9-7"/></svg>hello@quellmarkbuilders.ca</li>
    <li><svg width="11" height="11" viewBox="0 0 24 24" fill="#ccc"><path d="M5 3h4l2 5-3 2a11 11 0 0 0 6 6l2-3 5 2v4a2 2 0 0 1-2 2A17 17 0 0 1 3 5a2 2 0 0 1 2-2z"/></svg>Office: 780-555-0187</li>
    <li><svg width="11" height="11" viewBox="0 0 24 24" fill="#ccc"><path d="M12 2a7 7 0 0 0-7 7c0 5 7 13 7 13s7-8 7-13a7 7 0 0 0-7-7z"/></svg>Sat-Sun &amp; Holidays: Closed</li>
    </ul>
    <div class="social"><span></span><span></span><span></span><span></span></div>
  </div>
</footer>

<form class="contact-form">
  <h5>CONTACT US</h5>
  <div class="field">Name</div>
  <div class="field">Email</div>
  <div class="field">Phone</div>
  <div class="field msg">Message</div>
  <span class="submit">Submit Now</span>
</form>

<div class="section copyright">Copyright © 2020 - Quellmark Builders. All Rights Reserved.</div>

</body>
</html>
```